Progressive/contemporary business card design for successful Startups as a Service Company

New logo launched in 2020. New website launched in 2021. Now that COVID is (mostly) behind us, I'm networking with more people and need a business card that matches the company/logo design aesthetic.

```html
<!DOCTYPE html>
<html lang="en">
<head>
<meta charset="utf-8">
<title>Tessaryn business card</title>
<link href="https://fonts.googleapis.com/css2?family=Montserrat:wght@400;500&family=Open+Sans:wght@400;600&display=swap" rel="stylesheet">
<style>
  :root {
    --page-bg: #2a2a2c;
    --card-bg: #1d1d1f;
    --ink-white: #ffffff;
    --ink-soft: #e6e6e6;
    --accent-blue: #1e7fd0;
    --band-yellow: #ffc20e;
    --band-orange: #f47a20;
    --band-red: #e8262a;
    --band-sky: #3cc8f4;
    --band-deep: #0a6ec2;
  }
  * { box-sizing: border-box; margin: 0; padding: 0; }
  html, body { width: 1200px; height: 900px; overflow: hidden; }
  body {
    background: var(--page-bg);
    display: flex;
    flex-direction: column;
    align-items: center;
    justify-content: center;
    gap: 60px;
  }
  .card {
    position: relative;
    width: 560px;
    height: 320px;
    background: var(--card-bg);
    border-radius: 26px;
    overflow: hidden;
    box-shadow: 0 18px 40px rgba(0,0,0,.45);
  }
  .card-bands { position: absolute; inset: 0; width: 100%; height: 100%; }
  .wordmark {
    font-family: "Montserrat", sans-serif;
    font-weight: 400;
    color: var(--ink-white);
    text-transform: uppercase;
    white-space: nowrap;
  }
  .card-front .wordmark {
    position: absolute;
    left: 0; right: 0; top: 50%;
    transform: translateY(-50%);
    text-align: center;
    font-size: 40px;
    letter-spacing: 12px;
    padding-left: 12px;
  }
  .card-back .wordmark {
    position: absolute;
    right: 40px;
    top: 98px;
    font-size: 24px;
    letter-spacing: 7px;
  }
  .holder {
    position: absolute;
    left: 40px;
    top: 60px;
    font-family: "Open Sans", sans-serif;
  }
  .holder-name {
    color: var(--accent-blue);
    font-family: "Montserrat", sans-serif;
    font-weight: 500;
    font-size: 17px;
    letter-spacing: 1px;
    text-transform: uppercase;
  }
  .holder-role { color: var(--ink-soft); font-size: 12px; margin-top: 2px; }
  .divider {
    position: absolute;
    left: 40px; right: 40px; top: 146px;
    height: 1px;
    background: var(--accent-blue);
  }
  .contact {
    position: absolute;
    left: 40px;
    top: 160px;
    font-family: "Open Sans", sans-serif;
    font-size: 12px;
    line-height: 1.5;
    color: var(--ink-soft);
    list-style: none;
  }
  .contact-item { display: flex; align-items: center; gap: 7px; }
  .contact-item.plain { padding-left: 17px; }
  .contact-icon { width: 10px; height: 10px; flex: none; }
</style>
</head>
<body>

  <section class="card card-front" aria-label="Card front">
    <svg class="card-bands" viewBox="0 0 560 320" aria-hidden="true">
      <defs>
        <linearGradient id="warmFront" x1="0" y1="1" x2="1" y2="0">
          <stop offset="0" stop-color="var(--band-yellow)"/>
          <stop offset=".5" stop-color="var(--band-orange)"/>
          <stop offset="1" stop-color="var(--band-red)"/>
        </linearGradient>
        <linearGradient id="coolFront" x1="0" y1="1" x2="1" y2="0">
          <stop offset="0" stop-color="var(--band-deep)"/>
          <stop offset="1" stop-color="var(--band-sky)"/>
        </linearGradient>
      </defs>
      <polygon points="0,0 230,0 0,95" fill="url(#warmFront)"/>
      <polygon points="560,320 330,320 560,225" fill="url(#coolFront)"/>
    </svg>
    <p class="wordmark">Tessaryn</p>
  </section>

  <section class="card card-back" aria-label="Card back">
    <svg class="card-bands" viewBox="0 0 560 320" aria-hidden="true">
      <defs>
        <linearGradient id="warmBack" x1="0" y1="1" x2="1" y2="0">
          <stop offset="0" stop-color="var(--band-yellow)"/>
          <stop offset=".5" stop-color="var(--band-orange)"/>
          <stop offset="1" stop-color="var(--band-red)"/>
        </linearGradient>
        <linearGradient id="coolBack" x1="0" y1="1" x2="1" y2="0">
          <stop offset="0" stop-color="var(--band-deep)"/>
          <stop offset="1" stop-color="var(--band-sky)"/>
        </linearGradient>
      </defs>
      <polygon points="0,0 200,0 0,40" fill="url(#warmBack)"/>
      <polygon points="560,320 300,320 560,262" fill="url(#coolBack)"/>
    </svg>

    <div class="holder">
      <p class="holder-name">Erin Calloway</p>
      <p class="holder-role">Director</p>
    </div>

    <p class="wordmark">Tessaryn</p>

    <div class="divider"></div>

    <ul class="contact">
      <li class="contact-item plain">74 Linden Row</li>
      <li class="contact-item plain">Harbor Falls, OR 97310</li>
      <li class="contact-item">
        <svg class="contact-icon" viewBox="0 0 10 10" aria-hidden="true"><path d="M2 1 L4 1 L4.6 3 L3.4 3.8 Q4.3 5.7 6.2 6.6 L7 5.4 L9 6 L9 8 Q9 9 8 9 Q1 8.5 1 2 Q1 1 2 1Z" fill="var(--accent-blue)"/></svg>
        555-214-0398
      </li>
      <li class="contact-item">
        <svg class="contact-icon" viewBox="0 0 10 10" aria-hidden="true"><rect x="0.6" y="2" width="8.8" height="6" fill="none" stroke="var(--accent-blue)" stroke-width="1"/><path d="M0.8 2.3 L5 5.5 L9.2 2.3" fill="none" stroke="var(--accent-blue)" stroke-width="1"/></svg>
        hello@tessaryn.co
      </li>
      <li class="contact-item">
        <svg class="contact-icon" viewBox="0 0 10 10" aria-hidden="true"><g fill="none" stroke="var(--accent-blue)" stroke-width=".9"><circle cx="5" cy="5" r="4.2"/><ellipse cx="5" cy="5" rx="1.8" ry="4.2"/><path d="M0.8 5 H9.2"/></g></svg>
        www.tessaryn.co
      </li>
    </ul>
  </section>

</body>
</html>
```